依頼詳細
おおよそのイメージは添付した他店ポスターです。¥2,980から飲み放題付きで宴会ができるという事をおすすめ。料理は¥2,500コースをおすすめしたい。(11月末に2号店オープンのため()の文字も入れ替えられるようにデザインお願いします)
記載項目
飲み放題付き
忘新年会宴会コース

おひとり様¥2,980から
(おひとり様¥3,480から)

2〜25名様まで
(2〜40名様まで)

¥2,500コース 全9品
付出し
塩だれキャベツ
おすすめ鮮魚の一品
名古屋手羽先
鶏ちゃん焼き
〆のきしめん
みそ串かつ
とうふの和風サラダ
デザート

¥2,000コース 全7品
付出し
塩だれキャベツ
名古屋手羽先
鶏ちゃん焼き
〆のきしめん
みそ串かつ
とうふの和風サラダ

飲み放題 全60種類
2時間(ラストオーダーは30分前) おひとり様 +¥980
2.5時間(ラストオーダーは30分前) おひとり様 +¥1,480

ご予約受付 076-391-4857
(076-357-9014)
サイズ
A2サイズ
ページ数
片面
希望イメージ
シンプル 複雑
単色 カラフル
暗い 明るい
日常 高級
遊び心 厳粛
未来的 伝統的
女性的 男性的
希望する色
オレンジ 金 黒
納品ファイル
• 高解像度JPG (.jpg)
• イラストレーター形式 (.ai)
補足説明
当店のサイトページです。 http://www.kumobashi.jp/strK000417296/
コース画像、ロゴ、素材追加します。
コース写真の追加です。
コース写真の縦サイズ追加します。この写真の方が良いかもしれません。
■ 選んだ理由

訴求ポイントの見やすさなどが選んだ理由です。その他のデザインもホントよかったのですがこちらに決めさせていただきました。

■ 提案者全員のお礼・コメント

たくさん提案ありがとうございました。今後もいろいろデザインお願いする事があると思いますが宜しくお願いいたします。

```html
<!DOCTYPE html>
<html lang="ja">
<head>
<meta charset="utf-8">
<title>くもばし酒場 忘新年会 宴会コース</title>
<link rel="stylesheet" href="https://fonts.googleapis.com/css2?family=Dela+Gothic+One&family=Noto+Sans+JP:wght@500;700;900&family=Yuji+Boku&display=swap">
<style>
:root{
  --red:#d2121a;
  --orange:#f08a00;
  --yellow:#ffe33a;
  --cream:#fff6e2;
  --black:#1a1410;
  --white:#ffffff;
  --wood:#6b3a16;
}
*{margin:0;padding:0;box-sizing:border-box}
html,body{width:859px;height:1200px;overflow:hidden;background:var(--white)}
ul{list-style:none}
.poster{position:relative;width:859px;height:1200px;overflow:hidden;font-family:"Noto Sans JP",sans-serif;color:var(--black);background:var(--cream)}
.food-photo{position:absolute;left:0;top:0;width:859px;height:1130px;
  background:radial-gradient(ellipse at 30% 25%,#c8762e 0%,#8a4418 45%,#4a2510 80%),var(--wood)}
.food-photo-right{position:absolute;right:0;top:620px;width:260px;height:300px;background:radial-gradient(ellipse at 60% 50%,#d9a35c,#8c5422 75%)}
.cream-panel{position:absolute;left:0;top:860px;width:859px;height:270px;background:var(--cream)}
.logo{position:absolute;left:48px;top:14px;display:flex;align-items:center;gap:12px;background:rgba(255,255,255,.92);padding:12px 20px;border-radius:6px}
.logo-mark{width:34px;height:34px;border-radius:50%;background:var(--black)}
.logo-sub{display:block;font-size:17px;font-weight:700}
.logo-name{display:block;font-size:38px;font-weight:900;line-height:1.1}
.drinks-tag{position:absolute;left:688px;top:28px;width:150px;height:46px;background:var(--black);color:var(--yellow);font-weight:900;font-size:25px;display:flex;align-items:center;justify-content:center}
.title{position:absolute;left:680px;top:82px;writing-mode:vertical-rl;font-family:"Yuji Boku",serif;font-size:150px;line-height:1;color:var(--red);-webkit-text-stroke:4px var(--white);paint-order:stroke fill;letter-spacing:-6px;font-weight:400}
.subtitle{position:absolute;left:742px;top:668px;writing-mode:vertical-rl;font-weight:900;font-size:58px;background:var(--white);padding:8px 4px;line-height:1}
.kanpai{position:absolute;left:22px;top:222px;background:var(--yellow);color:var(--red);font-weight:900;font-size:22px;padding:4px 12px;border-radius:20px;transform:rotate(-8deg)}
.capacity{position:absolute;left:300px;top:180px;font-family:"Dela Gothic One",sans-serif;font-size:52px;color:var(--yellow);-webkit-text-stroke:8px var(--red);paint-order:stroke fill;line-height:1.1}
.capacity small{font-size:36px}
.plans{position:absolute;left:330px;top:246px;background:rgba(255,255,255,.94);padding:6px 14px;border-radius:6px;font-size:18px;font-weight:700;line-height:1.5;white-space:nowrap}
.plans .num{display:inline-block;width:22px;height:22px;border-radius:50%;background:var(--red);color:var(--white);text-align:center;line-height:22px;font-size:15px;margin-right:6px}
.plans .price{color:var(--red);font-size:24px;font-weight:900;margin-left:10px}
.plans .note{font-size:11px;font-weight:500}
.nomihodai{position:absolute;left:66px;top:272px;width:164px;height:164px;border-radius:50%;background:var(--white);border:6px solid var(--red);display:flex;flex-direction:column;align-items:center;justify-content:center;font-weight:900;line-height:1.2}
.nomihodai .count{font-size:20px}
.nomihodai .count b{color:var(--red);font-size:40px}
.nomihodai .label{font-size:30px;color:var(--red)}
.deal{position:absolute;left:445px;top:318px;width:180px;height:160px}
.deal-text{position:absolute;left:445px;top:342px;width:180px;text-align:center;font-weight:900;color:var(--white);transform:rotate(-8deg);line-height:1.1}
.deal-text .small{display:block;font-size:26px}
.deal-text .big{display:block;font-size:54px;line-height:1;color:var(--yellow);-webkit-text-stroke:5px var(--red);paint-order:stroke fill}
.course{position:absolute;left:52px;width:600px}
.course-a{top:440px}
.course-b{top:626px}
.course-head{display:flex;align-items:flex-end;gap:12px}
.course-count{width:70px;height:70px;border-radius:50%;background:var(--red);color:var(--white);font-weight:900;font-size:24px;display:flex;align-items:center;justify-content:center;line-height:1;text-align:center}
.course-price{font-family:"Dela Gothic One",sans-serif;font-size:66px;line-height:1;color:var(--red);-webkit-text-stroke:7px var(--white);paint-order:stroke fill}
.course-price span{font-size:38px}
.course-b .course-price{font-size:56px}
.menu{margin-top:6px;background:rgba(255,255,255,.95);border-left:34px solid var(--orange);padding:8px 14px;display:grid;grid-template-columns:repeat(3,max-content);gap:2px 14px;font-size:17px;font-weight:700;position:relative;white-space:nowrap}
.menu-label{position:absolute;left:-29px;top:8px;writing-mode:vertical-rl;color:var(--white);font-size:13px;font-weight:900}
.per-person{position:absolute;left:28px;top:880px;writing-mode:vertical-rl;font-weight:900;font-size:50px;line-height:1}
.main-price{position:absolute;left:110px;top:920px;font-family:"Dela Gothic One",sans-serif;font-size:190px;line-height:1;color:var(--red);-webkit-text-stroke:8px var(--white);paint-order:stroke fill;letter-spacing:-4px}
.main-price .yen{font-size:110px}
.main-price-from{position:absolute;left:770px;top:1030px;font-weight:900;font-size:44px}
.reserve-bar{position:absolute;left:0;top:1130px;width:859px;height:70px;background:var(--black);display:flex;align-items:center;padding:0 18px;gap:16px;color:var(--white)}
.reserve-label{background:var(--red);font-weight:900;font-size:22px;padding:6px 12px}
.reserve-tel{font-weight:900;font-size:36px;color:var(--yellow);display:flex;align-items:center;gap:8px}
.reserve-logo{margin-left:auto;display:flex;align-items:center;gap:8px;background:var(--white);color:var(--black);padding:6px 12px;font-weight:900;font-size:24px}
.reserve-logo .mark{width:20px;height:20px;background:var(--black)}
</style>
</head>
<body>
<div class="poster">
  <div class="food-photo" role="img" aria-label="大皿に盛られた名古屋手羽先と乾杯のビールジョッキの写真"></div>
  <div class="food-photo-right" role="img" aria-label="コース料理の写真"></div>
  <div class="cream-panel"></div>

  <div class="logo"><span class="logo-mark"></span><span><span class="logo-sub">名古屋手羽先</span><span class="logo-name">くもばし酒場</span></span></div>

  <div class="drinks-tag">飲み放題付き</div>
  <h1 class="title">忘新年会</h1>
  <div class="subtitle">宴会コース</div>

  <div class="kanpai">カンパーイ♪</div>
  <div class="capacity">2～25<small>名様まで!!</small></div>
  <div class="plans">
    <div><span class="num">1</span>2時間 <span class="note">(ラストオーダーは30分前)</span><span class="price">+¥980</span></div>
    <div><span class="num">2</span>2.5時間 <span class="note">(ラストオーダーは30分前)</span><span class="price">+¥1,480</span></div>
  </div>

  <div class="nomihodai"><span class="count">全<b>60</b>種類</span><span class="label">飲み放題</span></div>

  <svg class="deal" viewBox="0 0 190 170" aria-hidden="true"><polygon fill="#f08a00" stroke="#ffffff" stroke-width="4" points="95,2 112,38 150,14 142,56 188,60 152,88 182,124 136,120 130,166 100,134 64,166 60,122 10,130 38,92 2,60 48,54 40,12 80,36"/></svg>
  <div class="deal-text"><span class="small">こりゃ～</span><span class="big">お得!!</span></div>

  <section class="course course-a">
    <div class="course-head"><div class="course-count">全9<br>品</div><div class="course-price">2,500<span>円</span></div></div>
    <ul class="menu"><span class="menu-label">お品書き</span>
      <li>・付出し</li><li>・塩だれキャベツ</li><li>・おすすめ鮮魚の一品</li>
      <li>・名古屋手羽先</li><li>・鶏ちゃん焼き</li><li>・〆のきしめん</li>
      <li>・みそ串かつ</li><li>・とうふの和風サラダ</li><li>・デザート</li>
    </ul>
  </section>

  <section class="course course-b">
    <div class="course-head"><div class="course-count">全7<br>品</div><div class="course-price">2,000<span>円</span></div></div>
    <ul class="menu"><span class="menu-label">お品書き</span>
      <li>・付出し</li><li>・塩だれキャベツ</li><li>・名古屋手羽先</li>
      <li>・鶏ちゃん焼き</li><li>・〆のきしめん</li><li>・とうふの和風サラダ</li>
      <li>・みそ串かつ</li>
    </ul>
  </section>

  <div class="per-person">お一人様</div>
  <div class="main-price">2,980<span class="yen">円</span></div>
  <div class="main-price-from">から</div>

  <footer class="reserve-bar">
    <span class="reserve-label">ご予約受付</span>
    <span class="reserve-tel"><svg width="30" height="30" viewBox="0 0 24 24" aria-hidden="true"><path fill="#ffe33a" d="M6.6 10.8a15.1 15.1 0 0 0 6.6 6.6l2.2-2.2a1 1 0 0 1 1-.25 11.4 11.4 0 0 0 3.6.57 1 1 0 0 1 1 1V20a1 1 0 0 1-1 1A17 17 0 0 1 3 4a1 1 0 0 1 1-1h3.5a1 1 0 0 1 1 1c0 1.25.2 2.450.57 3.57a1 1 0 0 1-.25 1z"/></svg>電話:076-391-4857</span>
    <span class="reserve-logo"><span class="mark"></span>くもばし酒場</span>
  </footer>
</div>
</body>
</html>
```